Landing Page for AI Image and Video Generation

I will attach an excalidraw file that you can upload at https://plorvendix.com/ and check what needs to be done. It is a rough sketch with instructions.

All the information about the landing page is in the file below.

Number of Pages Required

1 page

```html
<!DOCTYPE html>
<html lang="en">
<head>
<meta charset="utf-8">
<title>Lumivox – AI Image and Video Generation</title>
<link href="https://fonts.googleapis.com/css2?family=Plus+Jakarta+Sans:wght@500;600;700;800&family=Inter:wght@400;500;600&display=swap" rel="stylesheet">
<style>
:root{
  --bg:#000;
  --card:#121114;
  --text:#fff;
  --muted:#d8d4e0;
  --violet:#7b5cf5;
  --magenta:#c24ad8;
  --pink:#e64ab8;
  --line:#4a4654;
  --grad:linear-gradient(90deg,#6d63f6,#c64fd8);
  --head:"Plus Jakarta Sans",sans-serif;
  --body:"Inter",sans-serif;
}
*{margin:0;padding:0;box-sizing:border-box}
html,body{width:1200px;height:3648px;overflow:hidden;background:var(--bg);color:var(--text);font-family:var(--body)}
.page{position:relative;width:1200px;height:3648px;overflow:hidden}
.abs{position:absolute}
a{color:inherit;text-decoration:none}

/* hero */
.hero{position:absolute;left:0;top:0;width:1200px;height:652px;
  background:radial-gradient(ellipse 520px 420px at 860px 300px,#c0508a 0%,#5a2a7a 45%,transparent 75%),
  linear-gradient(90deg,#3a1450 0%,#1a0c26 35%,#2b1340 60%,#3a1a4e 100%)}
.hero::after{content:"";position:absolute;left:0;right:0;bottom:0;height:200px;background:linear-gradient(transparent,#000)}
.hero-art{position:absolute;left:560px;top:0;width:640px;height:600px;
  background:radial-gradient(ellipse 300px 260px at 330px 260px,rgba(240,120,100,.55),rgba(80,40,140,.35) 60%,transparent 80%)}
.header{position:absolute;left:110px;top:0;width:974px;height:102px;background:#0b0a0d;
  clip-path:polygon(0 0,100% 0,96% 100%,4% 100%);z-index:2}
.logo{position:absolute;left:48px;top:34px;font-family:var(--head);font-weight:700;font-size:21px;letter-spacing:1.5px}
.header .sep{position:absolute;left:188px;top:0;width:1px;height:102px;background:#26242b}
.info{position:absolute;top:14px;font-size:14.5px;display:flex;align-items:center;gap:7px}
.nav{position:absolute;top:70px;left:218px;display:flex;gap:0;font-size:14.5px;letter-spacing:.5px;font-weight:500}
.nav span{padding:0 14px}
.nav .active{color:#d66fd8}
.nav .bar{padding:0 6px;color:#aaa}
.caret{display:inline-block;border:5px solid transparent;border-top:6px solid #fff;border-bottom:0;margin-left:4px;vertical-align:2px}
.tab-dot{position:absolute;left:222px;top:44px;width:42px;height:6px;border-radius:0 0 20px 20px;background:var(--magenta)}
.app-btn{position:absolute;left:820px;top:56px;width:90px;height:38px;background:var(--grad);
  clip-path:polygon(8% 0,100% 0,92% 100%,0 100%);font-weight:600;font-size:15px;display:flex;align-items:center;justify-content:center}
.hero h1{position:absolute;left:108px;top:222px;font-family:var(--head);font-weight:800;font-size:62px;line-height:68px;letter-spacing:-1px;z-index:1}
.hero p{position:absolute;left:113px;top:366px;width:430px;font-size:17px;line-height:30px;color:#eee;z-index:1}
.btn{background:var(--grad);clip-path:polygon(6% 0,100% 0,94% 100%,0 100%);display:flex;align-items:center;justify-content:center;font-weight:600;letter-spacing:.5px}
.hero .btn{position:absolute;left:113px;top:445px;width:178px;height:51px;font-size:16px;z-index:1}
.play{position:absolute;left:834px;top:316px;width:66px;height:66px;border-radius:50%;background:var(--violet);z-index:1}

/* section titles */
.title{position:absolute;left:0;width:1200px;text-align:center;font-family:var(--head);font-weight:700;font-size:37px;letter-spacing:-.3px}

/* products */
.card{position:absolute;top:791px;width:255px;height:354px;background:var(--card)}
.card .img{height:192px}
.card .badge{position:absolute;left:55px;top:0;width:145px;height:24px;background:var(--violet);
  clip-path:polygon(0 0,100% 0,90% 100%,10% 100%);font-size:12px;font-weight:600;display:flex;align-items:center;justify-content:center}
.card h3{position:absolute;left:20px;top:220px;font-family:var(--head);font-weight:600;font-size:18px}
.card p{position:absolute;left:20px;top:252px;width:215px;font-size:12px;line-height:21px;color:var(--muted)}

/* solutions */
.tabs{position:absolute;top:1344px;left:0;width:1200px;display:flex;justify-content:center;gap:0;font-family:var(--head);font-weight:700;font-size:12px}
.tabs span{padding:9px 14px;margin:0 7px}
.tabs .on{background:#1f1a2c;border-bottom:3px solid var(--violet)}
.tabline{position:absolute;left:110px;top:1380px;width:978px;height:1px;background:var(--line)}
.sol-bg{position:absolute;left:0;top:1396px;width:1200px;height:588px;
  background:radial-gradient(ellipse 400px 300px at 900px 300px,rgba(30,80,120,.55),transparent 70%),
  radial-gradient(ellipse 500px 300px at 200px 200px,rgba(90,30,120,.5),transparent 70%),#08070c}
.sol-img{position:absolute;top:1438px;height:499px}
.divider{position:absolute;left:347px;top:1438px;width:6px;height:499px;background:#fff}
.handle{position:absolute;left:324px;top:1650px;width:52px;height:52px;border-radius:50%;background:var(--violet)}
.sol h2{position:absolute;left:626px;top:1438px;font-family:var(--head);font-weight:700;font-size:26px}
.sol p{position:absolute;left:629px;width:462px;font-size:13.5px;line-height:30px;color:#eee}
.sol .btn{position:absolute;left:629px;top:1868px;width:177px;height:51px;font-size:16px}

/* gallery */
.gal{position:absolute}
.gal.frame{outline:3px solid var(--violet);outline-offset:0}

/* help */
.help{position:absolute;top:2850px;width:272px;height:248px;background:var(--card);text-align:center}
.help .ico{position:absolute;left:101px;top:-35px;width:70px;height:70px;border-radius:50%;display:flex;align-items:center;justify-content:center}
.help h3{margin-top:54px;font-family:var(--head);font-weight:600;font-size:23px}
.help p{margin:8px auto 0;width:232px;font-size:13.5px;line-height:23px;color:#e6e2ee}
.help .pill{position:absolute;left:83px;top:205px;width:105px;height:28px;border-radius:14px;font-size:11px;font-weight:600;display:flex;align-items:center;justify-content:center}

/* footer */
.foot-bg{position:absolute;left:0;top:3100px;width:1200px;height:548px;background:linear-gradient(#000 0%,#1a0f24 40%,#3a1e4c 100%)}
.foot h4{position:absolute;top:3228px;font-family:var(--head);font-weight:700;font-size:17px;letter-spacing:.5px}
.foot .about{position:absolute;left:116px;top:3279px;width:320px;font-size:14.5px;line-height:30px}
.email{position:absolute;left:116px;top:3398px;width:308px;height:55px;border:1px solid #4a3f56;display:flex;align-items:center;padding-left:23px;font-size:14.5px}
.links{position:absolute;top:3276px;list-style:none;font-size:14.5px;line-height:30px}
.links li::before{content:"";display:inline-block;width:5px;height:5px;border-radius:50%;background:var(--violet);margin-right:12px;vertical-align:3px}
.social{position:absolute;top:3280px;width:32px;height:32px;border-radius:50%;background:#1b1122;border:1px solid #4a3a58}
.social.on{background:var(--violet);border:0}
.bottom{position:absolute;left:120px;top:3549px;width:964px;height:99px;background:#0b0a0d;clip-path:polygon(3% 0,97% 0,100% 100%,0 100%)}
.bottom .logo{left:71px;top:35px;font-size:26px}
.bottom .copy{position:absolute;left:518px;top:40px;font-size:14.5px}
</style>
</head>
<body>
<div class="page">

<section class="hero">
  <div class="hero-art" role="img" aria-label="Illustration of a woman wearing a colourful VR headset and headphones with floating paint spheres"></div>
  <header class="header">
    <div class="logo">LUMIVOX</div>
    <div class="sep"></div>
    <div class="info" style="left:216px">
      <svg width="11" height="14" viewBox="0 0 12 16"><path d="M6 0a6 6 0 0 0-6 6c0 4.5 6 10 6 10s6-5.5 6-10a6 6 0 0 0-6-6zm0 8.5A2.5 2.5 0 1 1 6 3.5a2.5 2.5 0 0 1 0 5z" fill="#fff"/></svg>
      12 B Lumivox Lorem ipsum dolor sit amet</div>
    <div class="info" style="left:573px">
      <svg width="13" height="13" viewBox="0 0 16 16"><path d="M3.5 1l3 3-1.8 2a10 10 0 0 0 5.3 5.3l2-1.8 3 3-2 2.5C6 14.5 1.5 10 1 3.5z" fill="#fff"/></svg>
      144-555-0192</div>
    <div class="info" style="left:735px">
      <svg width="14" height="11" viewBox="0 0 16 12"><rect width="16" height="12" rx="1" fill="#fff"/><path d="M1 1l7 6 7-6" stroke="#0b0a0d" stroke-width="1.6" fill="none"/></svg>
      hello@lumivox.com</div>
    <div class="tab-dot"></div>
    <nav class="nav">
      <span class="active">HOME</span>
      <span>PRODUCTS<i class="caret"></i></span><span class="bar">|</span>
      <span>SOLUTIONS<i class="caret"></i></span><span class="bar">|</span>
      <span>FAQ</span><span class="bar">|</span>
      <span>CONTACT US</span>
    </nav>
    <a class="app-btn" href="#">APP</a>
  </header>
  <h1>WELCOME TO<br>LUMIVOX</h1>
  <p>Lorem ipsum dolor sit amet, consectetur adipiscing elit, sed do eiusmod tempor incididunt</p>
  <a class="btn" href="#">GET STARTED</a>
  <div class="play"><svg width="66" height="66" viewBox="0 0 66 66"><path d="M28 23l16 10-16 10z" fill="#fff"/></svg></div>
  <svg class="abs" style="left:984px;top:530px;z-index:1" width="76" height="48" viewBox="0 0 76 48"><path d="M32 2L2 24l30 22z" fill="none" stroke="#b9a9c9" stroke-width="2"/><path d="M46 2l28 22-28 22z" fill="none" stroke="#c24ad8" stroke-width="3"/></svg>
</section>

<h2 class="title" style="top:690px">OUR PRODUCTS</h2>
<article class="card" style="left:77px"><div class="img" role="img" aria-label="Woman in a VR headset with neon teal lighting" style="background:linear-gradient(135deg,#0f6f86,#2a2a5a 60%,#8a3a70)"></div><div class="badge">CLICK HERE</div><h3>Images</h3><p>Lorem ipsum dolor sit amet, consectetur adipiscing elit, sed do eiusmod tempor incididunt ut labore et dolore</p></article>
<article class="card" style="left:351px"><div class="img" role="img" aria-label="Illustrated adventurer with yellow scarf" style="background:linear-gradient(135deg,#cfd6da,#a89a80 60%,#5a4a38)"></div><div class="badge">CLICK HERE</div><h3>Videos</h3><p>Lorem ipsum dolor sit amet, consectetur adipiscing elit, sed do eiusmod tempor incididunt ut labore et dolore</p></article>
<article class="card" style="left:625px"><div class="img" role="img" aria-label="Man in sunglasses against a red neon city" style="background:linear-gradient(135deg,#d8304a,#8a1a3a 60%,#2a1020)"></div><div class="badge">CLICK HERE</div><h3>Upscaler</h3><p>Lorem ipsum dolor sit amet, consectetur adipiscing elit, sed do eiusmod tempor incididunt ut labore et dolore</p></article>
<article class="card" style="left:898px"><div class="img" role="img" aria-label="Bearded man with glasses in a night city" style="background:linear-gradient(135deg,#3a2a4a,#6a4a5a 50%,#1a2a3a)"></div><div class="badge">CLICK HERE</div><h3>Movie Maker</h3><p>Lorem ipsum dolor sit amet, consectetur adipiscing elit, sed do eiusmod tempor incididunt ut labore et dolore</p></article>
<svg class="abs" style="left:580px;top:1179px" width="40" height="22" viewBox="0 0 40 22"><path d="M16 1L2 11l14 10z" fill="none" stroke="#aaa" stroke-width="2"/><path d="M22 1l14 10-14 10z" fill="none" stroke="#c24ad8" stroke-width="2.5"/></svg>

<h2 class="title" style="top:1275px">OUR SOLUTIONS</h2>
<div class="tabs"><span class="on">DEVELOP WITH US</span><span>CONSULTATIONS</span></div>
<div class="tabline"></div>
<section class="sol">
  <div class="sol-bg" role="img" aria-label="Dark circuit board pattern with teal and purple glow"></div>
  <div class="sol-img" role="img" aria-label="Person wearing glowing VR goggles, before version" style="left:112px;width:235px;background:linear-gradient(135deg,#c8c4d8,#4a3a7a 55%,#1a1830)"></div>
  <div class="sol-img" role="img" aria-label="Person wearing glowing VR goggles, enhanced version" style="left:353px;width:214px;background:linear-gradient(135deg,#d8d6d2,#6a7a8a 50%,#3a2a26)"></div>
  <div class="divider"></div>
  <div class="handle"><svg width="52" height="52" viewBox="0 0 52 52"><path d="M23 18l-8 8 8 8zM29 18l8 8-8 8z" fill="none" stroke="#fff" stroke-width="2.2"/></svg></div>
  <h2>DEVELOP WITH US</h2>
  <p style="top:1490px">Lorem ipsum dolor sit amet, consectetur adipiscing elit, sed do eiusmod tempor incididunt ut labore et dolore magna aliqua. Quis ipsum suspendisse ultrices gravida. Risus commodo viverra maecenas accumsan lacus vel facilisis.</p>
  <p style="top:1640px">Lorem ipsum dolor sit amet, consectetur adipiscing elit, sed do eiusmod tempor incididunt ut labore et dolore magna aliqua. Quis ipsum suspendisse ultrices gravida. Risus commodo viverra maecenas accumsan lacus vel facilisis.</p>
  <p style="top:1790px">Lorem ipsum dolor sit amet, consectetur adipiscing elit, sed do eiusmod tempor incididunt ut labore</p>
  <a class="btn" href="#">LEARN MORE</a>
</section>

<h2 class="title" style="top:2053px">OUR GALLERY</h2>
<div class="gal frame" role="img" aria-label="Neon futuristic city street" style="left:421px;top:2160px;width:183px;height:181px;background:linear-gradient(#1a2a6a,#6a3aa8 60%,#c04ac0)"></div>
<div class="gal" role="img" aria-label="Sports car under a sunset sky" style="left:656px;top:2155px;width:245px;height:271px;background:linear-gradient(#8a2a6a,#d86a5a 35%,#3a3a5a 60%,#1a1a2a)"></div>
<div class="gal" role="img" aria-label="Man in suit with VR headset" style="left:269px;top:2318px;width:112px;height:108px;background:linear-gradient(135deg,#5a8aa0,#1a2a3a)"></div>
<div class="gal" role="img" aria-label="Figure in jacket facing a neon city" style="left:444px;top:2390px;width:171px;height:169px;background:linear-gradient(135deg,#1a6a9a,#2a1a3a 60%,#a03a4a)"></div>
<div class="gal" role="img" aria-label="Motorcyclist speeding through dust" style="left:238px;top:2467px;width:172px;height:170px;background:linear-gradient(135deg,#e8e4e0,#8a8480 60%,#3a3432)"></div>
<div class="gal" role="img" aria-label="Cyborg woman portrait" style="left:656px;top:2474px;width:172px;height:170px;background:linear-gradient(135deg,#4a5460,#1a1e24 60%,#6a2a2a)"></div>
<div class="gal" role="img" aria-label="Purple galaxy over mountains" style="left:864px;top:2473px;width:112px;height:107px;background:linear-gradient(#6a3aa8,#2a1a5a 60%,#1a1040)"></div>

<h2 class="title" style="top:2733px">HOW YOU CAN HELP</h2>
<article class="help" style="left:158px">
  <div class="ico" style="background:var(--violet)"><svg width="26" height="26" viewBox="0 0 24 24"><path d="M22 2L2 10l7 3 3 7z M9 13l13-11" fill="none" stroke="#fff" stroke-width="1.8" stroke-linejoin="round"/></svg></div>
  <h3>Newsletter</h3>
  <p>Lorem ipsum dolor sit amet, consectetur adipiscing elit, sed do eiusmod tempor incididunt ut labore et dolore magna aliqua. Quis</p>
  <a class="pill" href="#" style="background:var(--violet)">SIGN UP</a>
</article>
<article class="help" style="left:464px">
  <div class="ico" style="background:var(--pink)"><svg width="24" height="18" viewBox="0 0 16 12"><rect width="16" height="12" rx="1" fill="#fff"/><path d="M1 1l7 6 7-6" stroke="#e64ab8" stroke-width="1.4" fill="none"/></svg></div>
  <h3>Contact</h3>
  <p>Lorem ipsum dolor sit amet, consectetur adipiscing elit, sed do eiusmod tempor incididunt ut labore et dolore magna aliqua. Quis</p>
  <a class="pill" href="#" style="background:var(--pink)">CONTACT US</a>
</article>
<article class="help" style="left:769px">
  <div class="ico" style="background:var(--violet)"><svg width="22" height="24" viewBox="0 0 20 22"><circle cx="10" cy="6" r="5" fill="#fff"/><path d="M1 22c0-6 4-9 9-9s9 3 9 9z" fill="#fff"/></svg></div>
  <h3>Get A Quote</h3>
  <p>Lorem ipsum dolor sit amet, consectetur adipiscing elit, sed do eiusmod tempor incididunt ut labore et dolore magna aliqua. Quis</p>
  <a class="pill" href="#" style="background:var(--violet)">SIGN UP</a>
</article>

<footer class="foot">
  <div class="foot-bg"></div>
  <h4 style="left:116px">ABOUT US</h4>
  <p class="about">Lorem ipsum dolor sit amet, consectetur adipiscing elit, sed do eiusmod tempor incididunt ut</p>
  <div class="email">Email address
    <svg class="abs" style="left:264px;top:18px" width="18" height="18" viewBox="0 0 24 24"><path d="M22 2L2 10l7 3 3 7z" fill="#fff"/></svg></div>
  <h4 style="left:512px">QUICK LINKS</h4>
  <ul class="links" style="left:512px"><li>Home</li><li>Products</li><li>Solutions</li><li>Faq</li><li>Contact Us</li></ul>
  <h4 style="left:711px">HELP LINKS</h4>
  <ul class="links" style="left:711px"><li>Terms &amp; Conditions</li><li>Privacy Policy</li><li>About Us</li><li>Support</li></ul>
  <h4 style="left:927px">FOLLOWERS</h4>
  <span class="social on" style="left:926px" aria-label="Social profile one"></span>
  <span class="social" style="left:969px" aria-label="Social profile two"></span>
  <span class="social" style="left:1014px" aria-label="Social profile three"></span>
  <div class="bottom">
    <div class="logo">LUMIVOX</div>
    <div class="copy">©Copyrights 2024 Lumivox &nbsp; | &nbsp; All Rights Reserved</div>
  </div>
</footer>

</div>
</body>
</html>
```